Diverse, up-scale salon needs eye-catching, unique business cards.

We are looking for a unique business card design for our stylist but that can also be multi functional and used for appointment reminder and referrals. I will need a design in a format that I can modify names and titles going forward. In the past we have had a dark background with the logo on one side, and stylist and contact information on the other but we are open to all ideas. I have included our mission statement as well as branded colors below. The statement doesn't need to go on the card, it's just a reference for target market. We need space for the stylists name, title, instagram handle and then the salons phone number, website and address. I am also open to adding a spot for a qr code linked to the stylist instagram or the salon booking link.

primary brand colors:
#333333 #233415 #36502a #93874a #000000
Mission statement:
Morvane Hair Studio, a high-end salon located in the lively Downtown Farmington, Michigan, is committed to providing exceptional services in a welcoming and relaxed environment to meet the needs of our diverse clientele.
Our salon specializes in contemporary custom haircuts, coloring, extensions, and barbering and beard grooming services. Our team of skilled stylists is passionate and inventive in their hair styling techniques. At the heart of our salon are values centered on quality, innovation, creativity, and above all, comfort. These core values are evident in every appointment across our customizable array of services.
Our goal is to establish a benchmark for exceptional hair care for every human.
Website: www.morvanehairstudio-demo.com
instagram: @morvanehairstudio
address: 41872 Pelton Brook Rd, Farmington MI
phone: 248-316-8847

Industry/Entity Type

Hair Salon

Contact Information for Business Card

Stylist name, title, phone, instagram, website, address, (optional qr code)

Requirements
Should not have
• Does not need mission statement on the card.

```html
<!DOCTYPE html>
<html lang="en">
<head>
<meta charset="utf-8">
<title>Morvane Hair Studio – Business Card</title>
<link href="https://fonts.googleapis.com/css2?family=Oswald:wght@300;500&family=Poppins:wght@400&display=swap" rel="stylesheet">
<style>
  :root {
    --backdrop: #bbb7b8;
    --card-black: #121212;
    --brand-gold: #93874a;
    --panel-gold: #958a4e;
    --ink: #111111;
    --paper: #ffffff;
  }
  html, body {
    margin: 0;
    padding: 0;
    width: 1061px;
    height: 1200px;
    overflow: hidden;
    background: var(--backdrop);
  }
  .canvas {
    position: relative;
    width: 1061px;
    height: 1200px;
  }
  .card {
    position: absolute;
    left: 144px;
    width: 772px;
    height: 441px;
    box-shadow: 0 4px 10px rgba(0,0,0,0.35);
    overflow: hidden;
  }
  .card-front {
    top: 134px;
    background: var(--card-black);
  }
  .card-back {
    top: 620px;
    background: var(--paper);
  }
  .brand-mark {
    position: absolute;
    display: flex;
    align-items: center;
    justify-content: center;
    border-radius: 50%;
    border-style: solid;
    text-align: center;
    font-family: "Oswald", sans-serif;
    font-weight: 500;
    letter-spacing: 2px;
    line-height: 1.15;
    text-transform: uppercase;
  }
  .card-front .brand-mark {
    left: 291px;
    top: 124px;
    width: 184px;
    height: 184px;
    border-width: 3px;
    border-color: var(--brand-gold);
    color: var(--brand-gold);
    font-size: 24px;
  }
  .gold-panel {
    position: absolute;
    left: 0;
    top: 0;
    width: 376px;
    height: 441px;
    background: var(--panel-gold);
  }
  .card-back .brand-mark {
    left: 108px;
    top: 137px;
    width: 154px;
    height: 154px;
    border-width: 3px;
    border-color: var(--paper);
    color: var(--paper);
    font-size: 20px;
  }
  .divider {
    position: absolute;
    left: 372px;
    top: 25px;
    width: 9px;
    height: 387px;
    background: var(--ink);
  }
  .stylist-name {
    position: absolute;
    left: 426px;
    top: 82px;
    margin: 0;
    font-family: "Oswald", sans-serif;
    font-weight: 300;
    font-size: 44px;
    line-height: 1;
    letter-spacing: 1.5px;
    color: var(--ink);
  }
  .salon-name {
    position: absolute;
    left: 427px;
    top: 133px;
    margin: 0;
    font-family: "Poppins", sans-serif;
    font-size: 14px;
    line-height: 1;
    color: var(--brand-gold);
    text-transform: uppercase;
  }
  .contact-list {
    position: absolute;
    left: 0;
    top: 0;
    margin: 0;
    padding: 0;
    list-style: none;
    font-family: "Poppins", sans-serif;
    font-size: 16px;
    line-height: 24px;
    color: var(--ink);
  }
  .contact-item {
    position: absolute;
    left: 424px;
    white-space: nowrap;
  }
  .contact-item svg {
    position: absolute;
    left: 0;
    width: 20px;
    height: 20px;
  }
  .contact-item span {
    position: absolute;
    left: 36px;
    top: 0;
  }
  .item-address { top: 178px; }
  .item-address svg { top: 4px; }
  .item-phone { top: 238px; }
  .item-phone svg { top: 2px; }
  .item-web { top: 275px; }
  .item-web svg { top: 2px; }
  .item-social { top: 312px; }
  .item-social svg { top: 2px; }
</style>
</head>
<body>
<div class="canvas">

  <section class="card card-front">
    <div class="brand-mark">Morvane<br>Hair Studio</div>
  </section>

  <section class="card card-back">
    <div class="gold-panel">
      <div class="brand-mark">Morvane<br>Hair Studio</div>
    </div>
    <div class="divider"></div>

    <h1 class="stylist-name">JULIAN MERCER</h1>
    <p class="salon-name">Morvane Hair Studio</p>

    <ul class="contact-list">
      <li class="contact-item item-address">
        <svg viewBox="0 0 20 20" aria-hidden="true">
          <path d="M10 1.5a6 6 0 0 0-6 6c0 4.5 6 11 6 11s6-6.5 6-11a6 6 0 0 0-6-6z" fill="#93874a"/>
          <circle cx="10" cy="7.5" r="2.3" fill="#ffffff"/>
        </svg>
        <span>41872 Pelton Brook Rd,<br>Farmington MI</span>
      </li>
      <li class="contact-item item-phone">
        <svg viewBox="0 0 20 20" aria-hidden="true">
          <path d="M4.5 2.5l3 3-1.8 2.2c1 2.2 2.6 3.8 4.8 4.8l2.2-1.8 3 3-2 2.3C9 16 4 11 2.2 4.5z" fill="#93874a"/>
          <path d="M11.5 3.5a5 5 0 0 1 5 5M11.5 6a2.5 2.5 0 0 1 2.5 2.5" fill="none" stroke="#93874a" stroke-width="1.3" stroke-linecap="round"/>
        </svg>
        <span>248-316-8847</span>
      </li>
      <li class="contact-item item-web">
        <svg viewBox="0 0 20 20" aria-hidden="true">
          <circle cx="10" cy="10" r="8.5" fill="#93874a"/>
          <path d="M1.5 10h17M10 1.5v17M3 6h14M3 14h14" stroke="#ffffff" stroke-width="1"/>
          <ellipse cx="10" cy="10" rx="4" ry="8.5" fill="none" stroke="#ffffff" stroke-width="1"/>
        </svg>
        <span>www.morvanehairstudio-demo.com</span>
      </li>
      <li class="contact-item item-social">
        <svg viewBox="0 0 20 20" aria-hidden="true">
          <circle cx="10" cy="10" r="9" fill="#93874a"/>
        </svg>
        <span>@morvanehairstudio</span>
      </li>
    </ul>
  </section>

</div>
</body>
</html>
```